We need a designer to help us with our ecommerce site, cartwell. We will probably use a custom template in order to save costs. (http://www.copperkettlebakehouse.com/ is a good reference of what we want.)
Basically, our company is Brave Q and we are selling tshirts with social messages, and most of the profits will be going to these social enterprises. We are not selling tshirts, but instead, we are selling social messages to the masses.
We will like to use tshirts as vehicles to promote social messages among the youth, as such the designs and colour scheme should be colourful, in order to resonate with the youth. The website will be set up through Cartwell.com, therefore our elected designer has to be familiar with the usage of the Cartwell web design tools. The website should be as simple as possible; visually engaging while light on text, with subtle animation (eg. highlight product for alternate image) to engage our customers that visit the site.
Our logo will be Brave Q, with the tagline (tshirts for humanity).
In summary:
- Simple website showcasing T-shirt with social messages
- Done using Cartwell.com
- Bright colour scheme
- Simple snazzy design based on references provided(I have attached the file for the site layout)
- Logo design
We are committed in driving social messages among the youth and we are looking for enthusiastic designers who can embody our concept and bring the design to life; elegantly integrating cool and social meanings together.
Lets work together and make this world a better place; We are not just tshirts with social meanings, we are humanity at its purest form.
Yours truly,
the team at Brave Q.
Youth. 18-24

```html
<!DOCTYPE html>
<html lang="en">
<head>
<meta charset="utf-8">
<title>Brave Q — T-shirts for humanity</title>
<link href="https://fonts.googleapis.com/css2?family=Source+Sans+3:wght@300;400;600;700;900&family=Arimo:wght@400&display=swap" rel="stylesheet">
<style>
:root{
  --orange:#ef8a00;
  --orange-light:#f7a51c;
  --yellow:#fbd36a;
  --yellow-pale:#fff0c2;
  --dark:#4a4a4a;
  --darker:#333;
  --grey:#e8e8e8;
  --grey-mid:#cfcfcf;
  --text:#333;
  --red:#b31313;
  --blue-soft:#5a82b0;
  --white:#fff;
}
*{margin:0;padding:0;box-sizing:border-box}
html,body{width:1200px;height:1148px;overflow:hidden}
body{
  font-family:"Source Sans 3",sans-serif;color:var(--text);
  background:linear-gradient(180deg,var(--yellow) 0,#fde39a 500px,var(--yellow-pale) 501px,#fff8e6 1148px);
  position:relative;
}
.page{position:absolute;left:91px;top:0;width:1020px;height:1148px;background:var(--white);box-shadow:0 0 8px rgba(0,0,0,.12)}
.topline{position:absolute;left:0;top:0;width:1200px;height:6px;background:var(--orange-light)}
.abs{position:absolute}
.brand{left:99px;top:26px;font-size:58px;font-weight:900;color:var(--orange);letter-spacing:-1px;line-height:1}
.partner{left:973px;top:38px;font-size:24px;font-weight:700;color:#8a8a8a;letter-spacing:1px;line-height:1}

.nav{left:99px;top:107px;width:1002px;height:57px;display:flex;box-shadow:0 3px 4px rgba(0,0,0,.25)}
.nav-main{width:649px;height:100%;background:linear-gradient(180deg,#666,#3a3a3a);display:flex;border-radius:3px 0 0 3px}
.nav-main a{color:#fff;text-decoration:none;font-size:14.5px;display:flex;align-items:center;justify-content:center;border-right:1px solid #2a2a2a;box-shadow:1px 0 0 #6e6e6e}
.nav-main a:last-child{border:none;box-shadow:none}
.nav-cart{flex:1;background:linear-gradient(180deg,var(--orange-light),var(--orange));display:flex;align-items:center;gap:12px;padding-left:18px;font-size:14.5px;color:#3a2a00;border-radius:0 3px 3px 0}
.nav-cart .sep{margin:0 4px}

.hero{left:99px;top:186px;width:1002px;height:346px;border:1px solid #ddd;border-radius:4px 4px 0 0;overflow:hidden;background:linear-gradient(160deg,#f6f6f6 0,#e2e2e2 55%,#f1f1f1 75%,#d9d9d9 100%)}
.hero-photo{left:26px;top:0;width:287px;height:309px;background:linear-gradient(180deg,#e9e9e9,#f4f4f4 50%,#dcdcdc)}
.hero-tag{left:322px;top:96px;font-family:"Arimo",sans-serif;color:var(--blue-soft);font-size:30px;line-height:1}
.sizes{left:322px;top:134px;list-style:none;font-family:"Arimo",sans-serif;font-size:18px;color:#777}
.sizes li{height:22.5px;display:flex;align-items:center;gap:10px;padding-left:14px}
.sizes li svg{flex:none}
.hero-title{left:568px;top:56px;font-size:29px;font-weight:300;color:#444;width:306px;border-bottom:1px solid #aaa;padding-bottom:13px}
.hero-copy{left:568px;top:126px;width:306px;font-size:12.5px;line-height:21px;color:#444;text-align:justify}
.btn{display:flex;align-items:center;justify-content:center;border-radius:4px;color:#fff;font-size:16.5px}
.btn-dark{left:569px;top:213px;width:97px;height:31px;background:#555}
.btn-orange{left:675px;top:213px;width:149px;height:31px;background:var(--orange);color:#2a1a00}
.hero-bar{left:0;bottom:0;width:100%;height:37px;background:linear-gradient(180deg,#666,#444)}
.dots{right:66px;bottom:12px;display:flex;gap:10px}
.dots span{width:12px;height:12px;border-radius:50%;background:#ddd}
.dots span:first-child{background:#f4b626}
.hero-shadow{left:130px;top:532px;width:940px;height:12px;background:radial-gradient(ellipse at top,rgba(0,0,0,.25),transparent 70%)}

.h-red{font-size:26px;font-weight:400;color:var(--red);line-height:1}
.welcome-title{left:102px;top:576px}
.welcome-copy{left:102px;top:616px;width:647px;font-size:13px;line-height:21px;text-align:justify;color:#222}
.featured-title{left:771px;top:576px}
.featured-photo{left:773px;top:619px;width:328px;height:404px;border:1px solid #ccc;background:linear-gradient(180deg,#d9dde0,#a9cfe8 40%,#9cc6e2 80%,#c9d6de)}

.order{left:99px;top:745px;width:266px;height:278px;background:var(--orange);border-radius:4px}
.order h2{font-weight:400;color:#fff;font-size:26px;padding:9px 0 0 17px;height:50px;border-bottom:1px solid #c76f00;box-shadow:0 1px 0 #f8a640}
.field{position:absolute;left:20px;display:flex;align-items:center;width:232px}
.field label{width:66px;font-size:11.5px;color:#3a2200}
.select{width:166px;height:25px;background:#fff;border:1px solid #d9d9d9;border-radius:2px;font-size:11.5px;font-style:italic;color:#555;display:flex;align-items:center;justify-content:space-between;padding:0 10px}
.select::after{content:"";border:5px solid transparent;border-top:6px solid #777;margin-top:5px}
.order-btn{left:155px;top:238px;width:97px;height:31px;background:linear-gradient(180deg,#666,#444);box-shadow:0 1px 2px rgba(0,0,0,.4)}

.arrivals-title{left:407px;top:758px;width:308px;font-size:26px;font-weight:300;color:#444;padding:0 0 8px 4px;border-bottom:1px solid #bbb;line-height:1}
.arrival{position:absolute;left:410px;width:305px;height:84px}
.arrival .thumb{position:absolute;left:0;top:0;width:81px;height:84px}
.arrival p{position:absolute;left:98px;top:0;width:210px;font-size:12.5px;line-height:19px;color:#333;text-align:justify}
.arrival a{position:absolute;left:98px;top:64px;font-size:12.5px;color:#1d3f8a;text-decoration:underline}

.footer{left:99px;top:1047px;width:1002px;height:85px;background:var(--grey);border-radius:4px}
.footer-links{left:17px;top:20px;font-size:13px;color:#333;display:flex;gap:9px}
.footer-links .bar{color:#999}
.copy{left:17px;top:52px;font-size:13px;color:#333}
.social{right:40px;top:26px;display:flex;gap:12px}
.social span{width:35px;height:35px;border-radius:50%;background:linear-gradient(180deg,#5aa4c8,#2f6d96);box-shadow:0 2px 3px rgba(0,0,0,.3)}
</style>
</head>
<body>
<div class="topline"></div>
<div class="page"></div>

<div class="abs brand">Brave Q</div>
<div class="abs partner">NORTHWIND CO.</div>

<nav class="abs nav">
  <div class="nav-main">
    <a href="#" style="width:104px">Home</a>
    <a href="#" style="width:109px">About us</a>
    <a href="#" style="width:106px">Products</a>
    <a href="#" style="width:103px">Partners</a>
    <a href="#" style="width:120px">Contact us</a>
    <a href="#" style="width:107px">Buy Now</a>
  </div>
  <div class="nav-cart">
    <svg width="28" height="24" viewBox="0 0 28 24"><path d="M1 3h5l4 12h13l3-9H8" fill="none" stroke="#222" stroke-width="2.4" stroke-linejoin="round"/><circle cx="11" cy="20" r="2.2" fill="#222"/><circle cx="21" cy="20" r="2.2" fill="#222"/></svg>
    <span>My Cart - ( 0 ) Items</span><span class="sep">|</span><span>Login</span><span class="sep">|</span><span>Register</span>
  </div>
</nav>

<section class="abs hero">
  <div class="abs hero-photo" role="img" aria-label="Young man wearing a white printed T-shirt, cropped below the face"></div>
  <div class="abs hero-tag">I LIKE SHARING</div>
  <ul class="abs sizes">
    <li><svg width="16" height="16" viewBox="0 0 16 16" fill="#6a8fb8"><path d="M8 0l3 4H5zM8 16l-3-4h6zM0 8l4-3v6zM16 8l-4 3V5z"/></svg>Small</li>
    <li><svg width="16" height="16" viewBox="0 0 16 16" fill="#6a8fb8"><path d="M8 0l3 4H5zM8 16l-3-4h6zM0 8l4-3v6zM16 8l-4 3V5z"/></svg>Medium</li>
    <li><svg width="16" height="16" viewBox="0 0 16 16" fill="#6a8fb8"><path d="M8 0l3 4H5zM8 16l-3-4h6zM0 8l4-3v6zM16 8l-4 3V5z"/></svg>Large</li>
    <li><svg width="16" height="16" viewBox="0 0 16 16" fill="#6a8fb8"><path d="M8 0l3 4H5zM8 16l-3-4h6zM0 8l4-3v6zM16 8l-4 3V5z"/></svg>Extra Large</li>
  </ul>
  <h1 class="abs hero-title">Quis autem vel eum iure</h1>
  <p class="abs hero-copy">Sed ut perspiciatis unde omnis iste natus error sit totam rem aperiam, eaqueipsa quae ab illo inventore veritatis et quasi architecto beatae.</p>
  <div class="abs btn btn-dark">View more</div>
  <div class="abs btn btn-orange">Buy New T-Shirts</div>
  <div class="abs hero-bar"><div class="abs dots"><span></span><span></span><span></span><span></span></div></div>
</section>
<div class="abs hero-shadow"></div>

<h2 class="abs h-red welcome-title">Welcome to our site</h2>
<p class="abs welcome-copy">Sed ut perspiciatis unde omnis iste natus error sit voluptatem accusantium doloremque laudantium, totam rem aperiam, eaque ipsa quae ab illo inventore veritatis et quasi architecto beatae vitae dicta sunt explicabo. Nemo enim ipsam voluptatem quia voluptas sit aspernatur aut odit aut fugit, sed quia consequuntur magni dolores eos qui ratione voluptatem sequi nesciunt. Neque porro quisquam est, qui dolorem ipsum quia dolor sit amet, consectetur, adipisci velit, sed quia non numquam eius modi tempora incidunt ut labore.</p>

<h2 class="abs h-red featured-title">Featured Products</h2>
<div class="abs featured-photo" role="img" aria-label="Featured product: man wearing a light blue T-shirt with a social message print"></div>

<form class="abs order">
  <h2>Order T-Shirt</h2>
  <div class="field" style="top:70px"><label>For :</label><div class="select" style="width:130px">Men</div></div>
  <div class="field" style="top:114px"><label>Color :</label><div class="select">White</div></div>
  <div class="field" style="top:158px"><label>Size :</label><div class="select">Short</div></div>
  <div class="field" style="top:202px"><label>Price :</label><div class="select">$0 - $100</div></div>
  <div class="abs btn order-btn">Order Now</div>
</form>

<h2 class="abs arrivals-title">New Arrivals</h2>
<div class="arrival" style="top:824px">
  <div class="thumb" role="img" aria-label="Green T-shirt with a peace print" style="background:linear-gradient(180deg,#3fb257,#2e9a45)"></div>
  <p>Neque porro quisquam est, qui dolor em ipsum quia dolor sit amet, consectetur, adipisci velit, sed.</p>
  <a href="#">View more</a>
</div>
<div class="arrival" style="top:930px">
  <div class="thumb" role="img" aria-label="Black T-shirt with a printed slogan" style="background:linear-gradient(180deg,#3a3f4a,#111318)"></div>
  <p>Neque porro quisquam est, qui dolor em ipsum quia dolor sit amet, consectetur, adipisci velit, sed.</p>
  <a href="#">View more</a>
</div>

<footer class="abs footer">
  <div class="abs footer-links">
    <span>Home</span><span class="bar">|</span><span>About us</span><span class="bar">|</span><span>Products</span><span class="bar">|</span><span>Partners</span><span class="bar">|</span><span>Contact us</span><span class="bar">|</span><span>Buy Now</span><span class="bar">|</span><span>My Cart</span>
  </div>
  <div class="abs copy">Copyright © 2012 www.braveq.com &nbsp;&nbsp;All rights reserved.</div>
  <div class="abs social" aria-label="Social links"><span></span><span></span><span></span></div>
</footer>
</body>
</html>
```